GHollis Busisness Card

I am an aerospace consultant and at this time only need business cards.

Industry/Entity Type

Business

Contact Information for Business Card

Hollis Partners,LLC
Gerald T. Hollis

348 Birch Hollow Road
Madison AL 35762

256-555-0148 (cell)
256-555-0173 (fax)

geraldhollis@mailbrook.net

```html
<!DOCTYPE html>
<html lang="en">
<head>
<meta charset="utf-8">
<title>Hollis Partners Business Card</title>
<link href="https://fonts.googleapis.com/css2?family=Open+Sans:wght@400;600;700&display=swap" rel="stylesheet">
<style>
  :root {
    --backdrop: #e4e4e4;
    --card: #ffffff;
    --brand-blue: #1a3fa3;
    --ink: #3a3a3a;
    --band-text: #ffffff;
    --band-sub: #c9d4f2;
  }
  * { margin: 0; padding: 0; box-sizing: border-box; }
  html, body {
    width: 1200px; height: 1200px; overflow: hidden;
    background: var(--backdrop);
    font-family: "Open Sans", Arial, sans-serif;
  }
  .stage {
    width: 1200px; height: 1200px;
    display: flex; align-items: center; justify-content: center;
  }
  .business-card {
    position: relative;
    width: 900px; height: 514px;
    background: var(--card);
    box-shadow: 0 6px 24px rgba(0,0,0,0.12);
  }
  .brand {
    position: absolute; top: 58px; right: 60px;
    display: flex; align-items: center; gap: 14px;
  }
  .brand-dot {
    width: 26px; height: 26px; border-radius: 50%;
    background: var(--brand-blue);
  }
  .brand-name {
    font-size: 38px; font-weight: 600; color: var(--brand-blue);
    letter-spacing: 0.5px;
  }
  .name-band {
    position: absolute; left: 0; right: 0; top: 150px; height: 52px;
    background: var(--brand-blue);
    display: flex; align-items: center; gap: 22px;
    padding-left: 60px;
  }
  .person-name { color: var(--band-text); font-size: 27px; font-weight: 700; }
  .person-title { color: var(--band-sub); font-size: 19px; font-weight: 400; }
  .contact {
    position: absolute;
    display: flex; flex-direction: column; gap: 12px;
    color: var(--ink); font-size: 21px;
  }
  .contact-left { left: 60px; top: 232px; }
  .contact-right { right: 60px; top: 330px; }
  .contact-line { display: flex; align-items: center; gap: 12px; }
  .icon { width: 24px; height: 24px; flex: none; }
</style>
</head>
<body>
<main class="stage">
  <article class="business-card">
    <div class="brand">
      <span class="brand-dot"></span>
      <span class="brand-name">Hollis Partners,LLC</span>
    </div>

    <div class="name-band">
      <span class="person-name">Gerald T. Hollis</span>
      <span class="person-title">Aerospace Consultant</span>
    </div>

    <div class="contact contact-left">
      <div class="contact-line">
        <svg class="icon" viewBox="0 0 24 24" aria-hidden="true">
          <circle cx="12" cy="12" r="12" fill="#1a3fa3"/>
          <path d="M12 5.5a4 4 0 0 0-4 4c0 3 4 8 4 8s4-5 4-8a4 4 0 0 0-4-4z" fill="#fff"/>
          <circle cx="12" cy="9.5" r="1.5" fill="#1a3fa3"/>
        </svg>
        <span>348 Birch Hollow Road Madison, AL 35762</span>
      </div>
      <div class="contact-line">
        <svg class="icon" viewBox="0 0 24 24" aria-hidden="true">
          <circle cx="12" cy="12" r="12" fill="#1a3fa3"/>
          <rect x="6" y="8" width="12" height="8.5" rx="1" fill="#fff"/>
          <path d="M6.5 8.5 12 13l5.5-4.5" fill="none" stroke="#1a3fa3" stroke-width="1.2"/>
        </svg>
        <span>geraldhollis@mailbrook.net</span>
      </div>
    </div>

    <div class="contact contact-right">
      <div class="contact-line">
        <svg class="icon" viewBox="0 0 24 24" aria-hidden="true">
          <circle cx="12" cy="12" r="12" fill="#1a3fa3"/>
          <rect x="8.5" y="5.5" width="7" height="13" rx="1.2" fill="#fff"/>
          <circle cx="12" cy="16.3" r="0.9" fill="#1a3fa3"/>
        </svg>
        <span>256-555-0148</span>
      </div>
      <div class="contact-line">
        <svg class="icon" viewBox="0 0 24 24" aria-hidden="true">
          <circle cx="12" cy="12" r="12" fill="#1a3fa3"/>
          <rect x="6" y="10" width="12" height="7.5" rx="1" fill="#fff"/>
          <rect x="8.5" y="6" width="7" height="5" fill="#fff"/>
          <rect x="9" y="12.5" width="6" height="1.2" fill="#1a3fa3"/>
        </svg>
        <span>256-555-0173</span>
      </div>
    </div>
  </article>
</main>
</body>
</html>
```